Plastic Surgery Landing Page

We are a husband and wife team who own a plastic surgery practice in California. The plastic surgeon is Dr. Martin Kessingale. His wife, Tessa is his nurse practitioner.

Our plastic surgery practice is looking for a designer to create landing pages for various procedures that we offer. We will be starting with one procedure, but if we like the work, we will be creating many more. Our first page will promote a surgery called a Brazilian Butt Lift. Our hope is that the page will educate patients briefly on the procedure, but more than anything, get them to give us their contact information so that our Nurse Practitioner, Tessa can connect with them on a more personal level.

Maintaining the high quality of our brand is important. I have attached several documents that specifically lay out colors, fonts, and overall appearance. We also encourage you to visit our website: www.brightwaveplasticsurgery.example to get an idea of what we like aesthetically.

With regards to images or stock photos, we do not like nudity or anything that is overtly sexy or might be considered offensive. Our patients are real women who want to look sexy, but not necessarily like porn stars. Looking forward to seeing what you come up with!

Industry/Entity Type

Plastic

```html
<!DOCTYPE html>
<html lang="en">
<head>
<meta charset="utf-8">
<title>Brightwave Plastic Surgery – Landing Page</title>
<link rel="stylesheet" href="https://fonts.googleapis.com/css2?family=Anton&family=Montserrat:wght@400;500&family=Parisienne&family=Roboto+Condensed:wght@700&family=Tinos&display=swap">
<style>
  :root {
    --white: #ffffff;
    --band: #e6e6e6;
    --navy: #3f4a6e;
    --brand: #3e4868;
    --charcoal: #3d3d3d;
    --sky: #00aeef;
    --ink: #231f20;
    --script: #2a2a2a;
    --label: #333333;
    --button-text: #d9d9d9;
  }
  * { box-sizing: border-box; margin: 0; padding: 0; }
  html, body {
    width: 1200px; height: 871px; overflow: hidden;
    background: var(--white);
  }
  .page { position: relative; width: 1200px; height: 871px; }

  .brand { position: absolute; left: 28px; top: 33px; width: 282px; text-align: center; color: var(--brand); font-family: "Montserrat", sans-serif; font-weight: 400; }
  .brand-mark { width: 66px; height: 66px; border-radius: 50%; background: var(--brand); margin: 0 auto 12px; }
  .brand-name { font-size: 33px; letter-spacing: 6px; line-height: 1; }
  .brand-sub { font-size: 16px; letter-spacing: 1px; margin-top: 10px; }

  .tagline {
    position: absolute; right: 25px; top: 62px; text-align: right;
    font-family: "Parisienne", cursive; font-size: 42px; line-height: 50px; color: var(--script);
  }

  .band { position: absolute; left: 0; top: 200px; width: 1200px; height: 619px; background: var(--band); }

  .hero-photo {
    position: absolute; left: 7px; top: 204px; width: 416px; height: 588px;
    background: linear-gradient(180deg, #dfe3e6 0%, #b9c2c2 18%, #6f7a5e 30%, #8a8a5a 42%, #c9b07a 55%, #b8a689 75%, #9e9180 100%);
  }

  .intro {
    position: absolute; left: 436px; top: 219px; width: 388px; height: 428px;
    background: var(--navy); color: var(--white);
    display: flex; align-items: center; justify-content: center; text-align: center;
    font-family: "Roboto Condensed", sans-serif; font-weight: 700; font-size: 47px; line-height: 58px;
    padding: 0 44px;
  }

  .newsletter { position: absolute; left: 436px; top: 662px; width: 388px; height: 130px; background: var(--charcoal); }
  .newsletter-title { position: absolute; left: 34px; top: 20px; font-family: "Tinos", serif; font-size: 25px; color: var(--white); letter-spacing: 0.5px; }
  .newsletter-email {
    position: absolute; left: 34px; top: 66px; width: 202px; height: 34px;
    background: var(--white); border-radius: 8px; padding-left: 10px;
    font-family: "Tinos", serif; font-size: 15px; line-height: 34px; color: #111;
  }
  .newsletter-button {
    position: absolute; left: 261px; top: 66px; width: 93px; height: 34px;
    background: var(--sky); border-radius: 8px; text-align: center;
    font-family: "Tinos", serif; font-size: 17px; line-height: 34px; color: var(--white);
  }

  .contact { position: absolute; left: 839px; top: 219px; width: 336px; height: 573px; background: var(--sky); }
  .contact-title { position: absolute; left: 18px; top: 10px; font-family: "Anton", sans-serif; font-size: 56px; line-height: 80px; color: var(--white); letter-spacing: 1px; }
  .field {
    position: absolute; background: var(--white); border-radius: 6px;
    font-family: "Montserrat", sans-serif; font-weight: 500; font-size: 12px; color: var(--label);
    padding: 16px 0 0 10px; letter-spacing: 0.3px;
  }
  .send {
    position: absolute; left: 20px; top: 503px; width: 287px; height: 58px;
    background: var(--ink); border-radius: 6px; text-align: center;
    font-family: "Montserrat", sans-serif; font-size: 20px; line-height: 58px; color: var(--button-text);
  }
</style>
</head>
<body>
<main class="page">
  <header>
    <div class="brand">
      <div class="brand-mark"></div>
      <div class="brand-name">BRIGHTWAVE</div>
      <div class="brand-sub">Plastic Surgery</div>
    </div>
    <p class="tagline">Love yourself,Be yourself,&amp; Shine brighter than<br>Ever before.</p>
  </header>

  <div class="band"></div>

  <div class="hero-photo" role="img" aria-label="Smiling couple standing together outdoors in a sunlit golden field with hills behind them"></div>

  <section class="intro">
    <p>Lorem ipsum dolor sit amet, consectetuer adipiscing elit.</p>
  </section>

  <section class="newsletter">
    <h2 class="newsletter-title">NEWSLETTER SIGNUP</h2>
    <div class="newsletter-email">Email address</div>
    <div class="newsletter-button">SIGNUP</div>
  </section>

  <section class="contact">
    <h2 class="contact-title">CONTACT US</h2>
    <div class="field" style="left:20px;top:112px;width:140px;height:52px;">FIRST NAME</div>
    <div class="field" style="left:167px;top:112px;width:140px;height:52px;">LAST NAME</div>
    <div class="field" style="left:20px;top:169px;width:140px;height:52px;">AGE</div>
    <div class="field" style="left:167px;top:169px;width:140px;height:52px;">GENDER</div>
    <div class="field" style="left:20px;top:226px;width:287px;height:53px;">EMAIL</div>
    <div class="field" style="left:20px;top:284px;width:287px;height:53px;">PHONE</div>
    <div class="field" style="left:20px;top:342px;width:287px;height:149px;">MESSAGE</div>
    <div class="send">SEND A MESSAGE</div>
  </section>
</main>
</body>
</html>
```